Maple Hollow Bloom Panels Business card

Looking to have a business card design incorporating my logo for my flower wall business.

Industry/Entity Type

Wedding & event planning

Contact Information for Business Card

My business logo, my name - Lena Whitcombe (owner), my tagline - Let us be your something extra, phone # 401-726-3148, email address - maplehollowbloompanels@mailvane.net, my website - maplehollowbloompanels.net, Instagram handle- @maplehollowbloompanels, FB handle Handle - maplehollowbloompanels

Font styles to use
Other font styles liked:
• Sentaina is the font that is used in my logo

Requirements
Must have
• Would like a double sided business card

```html
<!DOCTYPE html>
<html lang="en">
<head>
<meta charset="utf-8">
<title>Maple Hollow Bloom Panels – Business Card</title>
<link href="https://fonts.googleapis.com/css2?family=Montserrat:wght@400;500;700&family=Mrs+Saint+Delafield&family=Allison&display=swap" rel="stylesheet">
<style>
  :root {
    --backdrop: #acacac;
    --card-white: #ffffff;
    --card-pink: #f9dfe9;
    --ink: #1c1c1c;
    --accent-pink: #e68bb7;
    --tagline-pink: #e77fb1;
    --icon-taupe: #a48b74;
    --ring-gold: #e3c77a;
  }
  * { margin: 0; padding: 0; box-sizing: border-box; }
  html, body { width: 1200px; height: 1000px; overflow: hidden; }
  body { background: var(--backdrop); position: relative; font-family: "Montserrat", sans-serif; color: var(--ink); }

  .card {
    position: absolute; left: 294px; width: 613px; height: 352px;
    border-radius: 26px; overflow: hidden;
    box-shadow: 18px 22px 40px rgba(0,0,0,0.28);
  }
  .card--front { top: 85px; background: var(--card-white); }
  .card--back { top: 535px; background: var(--card-pink); }

  .contact { position: absolute; left: 30px; width: 370px; top: 0; text-align: center; }
  .owner-name {
    position: absolute; left: 0; width: 370px; top: 60px;
    font-family: "Mrs Saint Delafield", cursive; font-size: 66px; line-height: 1; font-weight: 400;
  }
  .owner-role {
    position: absolute; left: 0; width: 370px; top: 138px;
    font-size: 15px; letter-spacing: 3px; color: var(--accent-pink); font-weight: 500;
    padding-left: 40px;
  }
  .contact-lines { position: absolute; left: 0; width: 370px; top: 171px; font-size: 15px; line-height: 19px; }
  .contact-lines .phone { font-weight: 700; }
  .social-icons { position: absolute; left: 0; width: 370px; top: 247px; display: flex; justify-content: center; gap: 7px; }
  .social-icons span { width: 20px; height: 20px; border-radius: 4px; background: var(--icon-taupe); display: block; }
  .social-handle { position: absolute; left: 0; width: 370px; top: 273px; font-size: 15px; font-weight: 500; }

  .brand-mark {
    position: absolute; display: flex; align-items: center; justify-content: center; text-align: center;
    border-radius: 50%; font-family: "Montserrat", sans-serif; font-weight: 500; color: var(--ink);
    letter-spacing: 1px; text-transform: uppercase;
  }
  .brand-mark--front {
    left: 392px; top: 100px; width: 170px; height: 170px;
    border: 1.5px solid var(--ring-gold); font-size: 13px; line-height: 20px; padding: 0 24px;
  }
  .brand-mark--back {
    left: 207px; top: 58px; width: 200px; height: 200px;
    background: var(--card-white); font-size: 15px; line-height: 23px; padding: 0 30px;
  }

  .tagline {
    position: absolute; left: 0; width: 613px; top: 262px; text-align: center;
    font-family: "Allison", cursive; font-size: 50px; color: var(--tagline-pink); line-height: 1;
  }
</style>
</head>
<body>
  <section class="card card--front" aria-label="Business card front">
    <div class="contact">
      <h1 class="owner-name">Lena Whitcombe</h1>
      <p class="owner-role">OWNER</p>
      <p class="contact-lines">
        maplehollowbloompanels@mailvane.net<br>
        maplehollowbloompanels.net<br>
        <span class="phone">401-726-3148</span>
      </p>
      <div class="social-icons" aria-hidden="true"><span></span><span></span></div>
      <p class="social-handle">maplehollowbloompanels</p>
    </div>
    <div class="brand-mark brand-mark--front">Maple Hollow Bloom Panels</div>
  </section>

  <section class="card card--back" aria-label="Business card back">
    <div class="brand-mark brand-mark--back">Maple Hollow Bloom Panels</div>
    <p class="tagline">Let us be your something extra</p>
  </section>
</body>
</html>
```